Pure Air Rules! Zephra Clear!

I need a 12 x 18 & 8.5 x 11 window advertisement for "Zephra Clear" Smoke & Odor Eliminator. "Powerful! Non-Staining! Fabric Safe!" Air Rules! Zephra Clear! See attached poster file for different scents we offer and how they should look. Also we use green smoke against a black background. The final design should stand out against other store front advertisements and represent "The High-Life"

```html
<!DOCTYPE html>
<html lang="en">
<head>
<meta charset="utf-8">
<title>Zephra Clear – Smoke &amp; Odor Eliminator</title>
<link rel="stylesheet" href="https://fonts.googleapis.com/css2?family=Oswald:wght@500;700&family=Montserrat:wght@800&display=swap">
<style>
  :root{
    --ink:#050805;
    --deep-green:#0b2a0f;
    --smoke-green:#3fae3a;
    --glow-green:#7fe36d;
    --leaf-green:#5fbf2f;
    --alert-red:#e3262b;
    --sun-yellow:#f6c619;
    --pale-green:#dff3d6;
    --dark-outline:#10240f;
    --swoosh:#3d8a22;
  }
  *{margin:0;padding:0;box-sizing:border-box}
  html,body{width:900px;height:1200px;overflow:hidden;background:var(--ink)}
  .poster{
    position:relative;width:900px;height:1200px;overflow:hidden;
    background:var(--ink);
    font-family:"Oswald",sans-serif;
    text-align:center;
  }
  .smoke-backdrop{
    position:absolute;inset:0;
    background:
      radial-gradient(ellipse 38% 30% at 50% 62%, rgba(127,227,109,.55), transparent 70%),
      radial-gradient(ellipse 45% 40% at 62% 30%, rgba(63,174,58,.55), transparent 72%),
      radial-gradient(ellipse 40% 35% at 30% 75%, rgba(63,174,58,.45), transparent 70%),
      radial-gradient(ellipse 70% 60% at 50% 50%, var(--deep-green), var(--ink) 90%);
  }
  .brand{
    position:absolute;top:150px;left:0;right:0;
    display:flex;align-items:center;justify-content:center;gap:22px;
  }
  .brand-dot{width:34px;height:34px;border-radius:50%;background:var(--glow-green)}
  .brand-name{
    font-weight:700;font-size:104px;line-height:1;letter-spacing:2px;
    color:var(--pale-green);text-transform:uppercase;
  }
  .headline{
    position:absolute;top:400px;left:0;right:0;
    font-weight:700;font-size:60px;line-height:1;text-transform:uppercase;
    text-shadow:3px 3px 0 var(--dark-outline),-1px -1px 0 var(--dark-outline);
    letter-spacing:-1px;
  }
  .headline .smoke{color:var(--leaf-green)}
  .headline .amp{color:var(--sun-yellow)}
  .headline .odor{color:var(--alert-red)}
  .benefits{
    position:absolute;top:482px;left:0;right:0;list-style:none;
    font-family:"Montserrat",sans-serif;font-weight:800;font-size:40px;line-height:60px;
    color:var(--sun-yellow);text-transform:uppercase;
    text-shadow:2px 2px 0 var(--dark-outline),-1px -1px 0 var(--dark-outline),1px -1px 0 var(--dark-outline),-1px 1px 0 var(--dark-outline);
  }
  .tagline{
    position:absolute;left:0;right:0;
    font-weight:700;line-height:1;text-transform:uppercase;color:var(--pale-green);
    -webkit-text-stroke:2px var(--dark-outline);
    text-shadow:3px 3px 0 var(--dark-outline);
  }
  .tagline-first{top:678px;font-size:56px}
  .tagline-second{top:760px;font-size:64px}
  .base-swoosh{position:absolute;left:0;bottom:0;width:900px;height:140px}
  .product-lineup{
    position:absolute;left:215px;top:880px;width:470px;height:290px;
    display:flex;align-items:flex-end;justify-content:space-between;
  }
  .product-can{
    width:98px;height:290px;border-radius:46px 46px 8px 8px;
    background:linear-gradient(90deg,#b9c2bd,#f4f7f5 40%,#ffffff 55%,#c7cfca);
  }
  .product-can.short{height:262px}
</style>
</head>
<body>
<main class="poster">
  <div class="smoke-backdrop" role="img" aria-label="Swirling green smoke rising over a black background"></div>

  <header class="brand">
    <span class="brand-dot"></span>
    <span class="brand-name">Zephra Clear</span>
  </header>

  <h1 class="headline"><span class="smoke">Smoke</span> <span class="amp">&amp;</span> <span class="odor">Odor Eliminator.</span></h1>

  <ul class="benefits">
    <li>Powerful!</li>
    <li>Non-Staining!</li>
    <li>Fabric Safe!"</li>
  </ul>

  <p class="tagline tagline-first">Air Rules!</p>
  <p class="tagline tagline-second">Zephra Clear!</p>

  <svg class="base-swoosh" viewBox="0 0 900 140" aria-hidden="true">
    <path d="M0 140 Q300 40 900 30 L900 140 Z" fill="var(--ink)"/>
    <path d="M0 140 Q300 40 900 30 L900 42 Q320 52 0 140 Z" fill="var(--swoosh)"/>
  </svg>

  <div class="product-lineup" role="img" aria-label="Four white Zephra Clear spray cans in assorted scents">
    <div class="product-can"></div>
    <div class="product-can"></div>
    <div class="product-can short"></div>
    <div class="product-can"></div>
  </div>
</main>
</body>
</html>
```